Skin rejuvenation webpage

I already have functioning websites, 9vital.clinic and hearthcarecentral.com. I need to create a page to add that captures the general overarching theme of these two websites, while educating and advertising our new offering of skin rejuvenation in our clinic. 9 Vital and Hearthside Care Central are both one clinic. 9 Vital is a membership model healthcare clinic and Hearthside Care Central is a regular traditional medical clinic that uses health insurance. The skin rejuvenation is CASH PAY only, so no insurance is billed. We give large discounts to those who are current members of 9 Vital.

For title, something like, "“Smooth wrinkles. Restore skin. Age intelligently." And subtitle something like "Lumexa + Advanced Laser (Qorvin) for complete skin rejuvenation".

Lumexa → relaxes muscles Laser → improves skin quality
Combine them = better results
Step 1: Lumexa Smooth dynamic wrinklesPrevent deeper lines
Step 2: Qorvin Laser Reduce redness, pigmentation Improve collagen + texture

Or Bold headline ("QORVIN Laser | The New Gold Standard"), subhead emphasizing "no downtime, no numbing, treats over 25 indications including fine lines and wrinkles," with immediate phone/CTA buttons.

Layout: Clean sections—overview of how it works (wavelength explanations: yellow for vascular/redness, infrared for collagen), benefits bullets, detailed before/after photo galleries (e.g., "Before and After 1 Treatment for Skin Rejuvenation" showing smoother, firmer skin).

Before/after photos: https://brelunix.com/results/
“Start with a personalized skin plan”

Book now
Limited appointments (scarcity)

```html
<!DOCTYPE html>
<html lang="en">
<head>
<meta charset="utf-8">
<title>9 Vital — Skin Rejuvenation</title>
<link href="https://fonts.googleapis.com/css2?family=Manrope:wght@500;600;700;800&family=Inter:wght@400;500;600;700&display=swap" rel="stylesheet">
<style>
:root{
  --ink:#15201f;
  --teal:#1f5c63;
  --teal-mid:#2f7a82;
  --teal-soft:#8fc1c6;
  --muted:#5a6464;
  --bg-soft:#eef0ef;
  --bg-band:#e3e5e4;
  --card:#ffffff;
  --panel:#e8e9e9;
  --gold:#b36b12;
  --alert:#c0392b;
}
*{box-sizing:border-box;margin:0;padding:0}
html,body{width:1200px;height:4401px;overflow:hidden}
body{font-family:"Inter",sans-serif;color:var(--ink);background:#fff;position:relative}
h1,h2,h3{font-family:"Manrope",sans-serif}

.wordmark{font-family:"Inter",sans-serif;font-weight:500;font-size:24px;color:var(--ink);letter-spacing:0}

.nav{position:absolute;top:0;left:0;width:1200px;height:68px;background:rgba(255,255,255,.92);display:flex;align-items:center;padding:0 32px;z-index:5}
.nav-links{position:absolute;left:480px;display:flex;gap:30px;font-size:13px;color:var(--muted)}
.nav-links .active{color:var(--teal);border-bottom:2px solid var(--teal);padding-bottom:6px}
.nav-cta{position:absolute;right:34px;top:18px;background:var(--teal);color:#fff;font-size:12px;font-weight:600;padding:10px 20px;border-radius:20px}

.hero{position:absolute;top:0;left:0;width:1200px;height:700px;overflow:hidden}
.hero-photo{position:absolute;inset:0;background:linear-gradient(90deg,#e6e9e8 0%,#d9dedd 35%,#b9c3c1 60%,#c9c6bf 80%,#d8d3cc 100%)}
.hero-copy{position:absolute;left:32px;top:180px}
.hero h1{font-size:68px;line-height:68px;font-weight:800;letter-spacing:-2px}
.hero h1 .accent{color:var(--teal)}
.hero-sub{margin-top:22px;font-size:17px;line-height:26px;color:#3c4646;width:520px}
.hero-sub span{color:var(--teal-mid)}
.hero-actions{margin-top:38px;display:flex;align-items:center;gap:18px}
.btn{display:inline-block;background:linear-gradient(90deg,var(--teal),#4a9099);color:#fff;font-weight:600;border-radius:30px;box-shadow:0 8px 18px rgba(31,92,99,.25)}
.hero .btn{font-size:15px;padding:18px 36px}
.scarcity{display:flex;align-items:center;gap:8px;font-size:12px;font-weight:600;letter-spacing:.6px;color:var(--teal)}

.treatments{position:absolute;top:700px;left:0;width:1200px;height:720px;background:var(--bg-soft)}
.step{position:absolute;left:32px;width:538px;height:186px;background:var(--card);border-radius:18px;padding:30px 30px}
.step h3{display:flex;align-items:center;gap:14px;font-size:21px;font-weight:600;color:var(--teal)}
.step .num{width:34px;height:34px;border-radius:50%;background:#e7eeef;color:var(--ink);font-size:18px;display:flex;align-items:center;justify-content:center}
.step p{margin-top:18px;font-size:13.5px;line-height:24px;color:#3d4747;width:440px}
.device{position:absolute;left:630px;top:92px;width:540px;height:538px;border-radius:22px;background:linear-gradient(135deg,#d6d8d6,#b9bdba 55%,#8fa3a5);box-shadow:0 20px 40px rgba(0,0,0,.15)}
.synergy{position:absolute;left:608px;top:549px;width:246px;height:103px;background:var(--teal);border-radius:16px;color:#fff;padding:30px 28px}
.synergy strong{font-family:"Manrope",sans-serif;font-size:18px;font-weight:600;display:block}
.synergy small{font-size:10px;letter-spacing:1.6px;opacity:.8}

.science{position:absolute;top:1420px;left:0;width:1200px;height:684px;background:#fff}
.science h2{position:absolute;top:86px;width:100%;text-align:center;font-size:46px;font-weight:700}
.rule{position:absolute;top:160px;left:556px;width:88px;height:4px;background:var(--teal-soft);border-radius:2px}
.light{position:absolute;top:222px;width:434px;height:372px;background:#f2f3f3;border-radius:18px;padding:38px 38px}
.light .ico{width:58px;height:58px;border-radius:10px;display:flex;align-items:center;justify-content:center}
.light h3{margin-top:32px;font-size:22px;font-weight:600}
.light p{margin-top:18px;font-size:14px;line-height:24px;color:#4a5353;width:345px}
.light .target{position:absolute;left:38px;right:38px;bottom:38px;border-top:1px solid #dcdfdf;padding-top:24px;font-size:12px;font-weight:700;letter-spacing:.6px}

.benefits{position:absolute;top:2104px;left:0;width:1200px;height:323px;background:var(--bg-band)}
.benefit{position:absolute;top:91px;width:240px;text-align:center}
.benefit .circle{width:74px;height:74px;border-radius:50%;background:#fff;margin:0 auto;display:flex;align-items:center;justify-content:center;box-shadow:0 4px 10px rgba(0,0,0,.05)}
.benefit h4{margin-top:30px;font-size:14px;font-weight:600}
.benefit span{display:block;margin-top:8px;font-size:11px;color:#5a6464}

.results{position:absolute;top:2427px;left:0;width:1200px;height:648px;background:#fff}
.eyebrow{position:absolute;left:32px;top:89px;font-size:11px;font-weight:700;letter-spacing:1.2px;color:var(--teal)}
.results h2{position:absolute;left:32px;top:108px;font-size:44px;font-weight:700}
.results .note{position:absolute;right:32px;top:139px;font-size:14px;color:#5a6464}
.compare{position:absolute;top:218px;width:547px;height:305px;border-radius:18px;overflow:hidden}
.compare .half{position:absolute;top:0;bottom:0}
.compare .divider{position:absolute;left:272px;top:0;bottom:0;width:3px;background:#fff}
.compare .knob{position:absolute;left:258px;top:138px;width:30px;height:30px;border-radius:50%;background:#fff;display:flex;align-items:center;justify-content:center}
.tag{position:absolute;bottom:16px;background:rgba(60,60,60,.7);color:#fff;font-size:9px;font-weight:700;letter-spacing:1px;padding:4px 12px;border-radius:10px}
.tag.after{background:var(--teal)}
.caption{position:absolute;top:542px;width:547px;text-align:center;font-size:12.5px;color:#333}

.pricing{position:absolute;top:3075px;left:0;width:1200px;height:719px;background:var(--bg-soft)}
.price-card{position:absolute;left:32px;top:90px;width:1138px;height:540px;background:#fff;border-radius:40px;overflow:hidden;box-shadow:0 20px 40px rgba(0,0,0,.06)}
.price-card .wash{position:absolute;right:0;top:0;width:520px;height:100%;background:#f1f4f5;clip-path:polygon(14% 0,100% 0,100% 100%,0 100%)}
.price-copy{position:absolute;left:75px;top:127px;width:480px}
.price-copy h2{font-size:34px;font-weight:700}
.price-copy > p{margin-top:20px;font-size:16px;line-height:27px;color:#3c4646}
.perk{display:flex;gap:14px;margin-top:26px}
.perk .dot{flex:none;width:18px;height:18px;border-radius:50%;background:#d9ecee;display:flex;align-items:center;justify-content:center;margin-top:2px}
.perk h4{font-size:14px;font-weight:600}
.perk p{font-size:12px;line-height:18px;color:#555;margin-top:2px}
.perk p.teal{color:var(--teal);font-weight:600}
.package{position:absolute;left:600px;top:73px;width:463px;height:392px;background:var(--panel);border-radius:22px;padding:32px 30px;text-align:center}
.package .eyebrow2{font-size:10.5px;font-weight:700;letter-spacing:1.4px;color:var(--teal)}
.package .amount{font-family:"Manrope",sans-serif;font-size:46px;font-weight:800;margin-top:6px}
.package .pkg{font-size:12px;letter-spacing:1.6px;color:#444;margin-top:4px}
.lines{margin-top:28px;text-align:left}
.line{display:flex;justify-content:space-between;font-size:12.5px;padding:10px 0;border-bottom:1px solid #d7d9d9}
.line b{font-weight:700}
.line.save{border:none;color:var(--teal);font-weight:600;padding-top:16px}
.claim{display:block;margin-top:26px;background:var(--teal);color:#fff;font-size:16px;font-weight:500;padding:18px 0;border-radius:10px}

.cta{position:absolute;top:3794px;left:0;width:1200px;height:481px;background:#fff;text-align:center}
.cta h2{width:780px;margin:84px auto 0;font-size:56px;line-height:60px;font-weight:800;letter-spacing:-2px}
.cta p{width:740px;margin:36px auto 0;font-size:18px;line-height:28px;color:#3c4646}
.cta-actions{position:absolute;top:330px;left:334px;display:flex;align-items:center;gap:22px;text-align:left}
.cta .btn{font-size:17px;padding:20px 44px}
.phone{font-family:"Manrope",sans-serif;font-size:22px;font-weight:600;color:var(--teal)}
.phone small{display:block;font-family:"Inter",sans-serif;font-size:10.5px;font-weight:700;letter-spacing:1px;color:var(--alert);margin-top:4px}

.footer{position:absolute;top:4275px;left:0;width:1200px;height:126px;background:#f3f6f7}
.footer .wordmark{position:absolute;left:48px;top:30px;font-size:22px}
.footer .legal{position:absolute;left:48px;top:82px;font-size:10.5px;letter-spacing:1.2px;color:#8a9696}
.footer nav{position:absolute;right:46px;top:58px;display:flex;gap:30px;font-size:10.5px;letter-spacing:1.2px;color:#8a9696}
</style>
</head>
<body>

<header class="nav">
  <div class="wordmark">9 Vital</div>
  <nav class="nav-links"><span class="active">Treatments</span><span>Technology</span><span>Results</span><span>Pricing</span></nav>
  <div class="nav-cta">Book Appointment</div>
</header>

<section class="hero">
  <div class="hero-photo" role="img" aria-label="Portrait of a smiling woman in a bright clinic interior"></div>
  <div class="hero-copy">
    <h1>Smooth Wrinkles.<br>Restore Skin.<br><span class="accent">Age Intelligently.</span></h1>
    <p class="hero-sub">The synergy of <span>Lumexa</span> and <span>Advanced Qorvin Laser</span> for complete cellular skin rejuvenation.</p>
    <div class="hero-actions">
      <span class="btn">Book Now</span>
      <span class="scarcity"><svg width="14" height="14" viewBox="0 0 14 14"><circle cx="7" cy="7" r="6" fill="#1f5c63"/><path d="M7 3.5V7l2.2 1.4" stroke="#fff" stroke-width="1.4" fill="none" stroke-linecap="round"/></svg>LIMITED APPOINTMENTS AVAILABLE</span>
    </div>
  </div>
</section>

<section class="treatments">
  <article class="step" style="top:152px">
    <h3><span class="num">1</span>Lumexa Precision</h3>
    <p>Relaxes targeted facial muscles to instantly smooth dynamic wrinkles and prevent new lines from forming. Professional, conservative dosing for natural movement.</p>
  </article>
  <article class="step" style="top:384px">
    <h3><span class="num">2</span>Qorvin Technology</h3>
    <p>The gold standard in laser therapy. Simultaneously targets vascular redness and builds deep collagen structure for a luminous, even-toned complexion.</p>
  </article>
  <div class="device" role="img" aria-label="Laser treatment device with touchscreen in a clinic treatment room"></div>
  <div class="synergy"><strong>Dual-Action Synergy</strong><small>BETTER RESULTS TOGETHER</small></div>
</section>

<section class="science">
  <h2>Advanced Light Science</h2>
  <div class="rule"></div>
  <article class="light" style="left:152px">
    <div class="ico" style="background:#f6e9bf"><svg width="22" height="22" viewBox="0 0 22 22" stroke="#c48a12" stroke-width="1.6" fill="none" stroke-linecap="round"><circle cx="11" cy="11" r="4"/><path d="M11 2v2.5M11 17.5V20M2 11h2.5M17.5 11H20M4.6 4.6l1.8 1.8M15.6 15.6l1.8 1.8M4.6 17.4l1.8-1.8M15.6 6.4l1.8-1.8"/></svg></div>
    <h3>589nm Yellow Light</h3>
    <p>Specifically absorbed by oxyhemoglobin to eliminate unwanted redness, broken capillaries, and active acne without thermal damage to surrounding tissue.</p>
    <div class="target" style="color:var(--gold)">TARGET: VASCULAR &amp; ROSACEA</div>
  </article>
  <article class="light" style="left:616px">
    <div class="ico" style="background:#cfdfe1"><svg width="22" height="22" viewBox="0 0 22 22" stroke="#1f5c63" stroke-width="1.6" fill="none" stroke-linecap="round"><circle cx="11" cy="11" r="2.5"/><path d="M11 3v4M11 15v4M3 11h4M15 11h4"/></svg></div>
    <h3>1319nm Infrared Light</h3>
    <p>Penetrates deep into the dermal layers to trigger massive collagen synthesis and elastin production, refining skin texture and tightening pores.</p>
    <div class="target" style="color:var(--teal)">TARGET: TEXTURE &amp; COLLAGEN</div>
  </article>
</section>

<section class="benefits">
  <div class="benefit" style="left:43px"><div class="circle"><svg width="22" height="22" viewBox="0 0 22 22" fill="none" stroke="#1f5c63" stroke-width="1.6"><circle cx="11" cy="11" r="8"/><path d="M7.5 11l2.5 2.5 4.5-5" stroke-linecap="round"/></svg></div><h4>No Downtime</h4><span>Lunchtime procedure</span></div>
  <div class="benefit" style="left:335px"><div class="circle"><svg width="22" height="22" viewBox="0 0 22 22" fill="none" stroke="#1f5c63" stroke-width="1.6"><rect x="4" y="6" width="14" height="12" rx="2"/><path d="M8 6V4h6v2M11 9v6M8 12h6"/></svg></div><h4>No Numbing</h4><span>Pain-free technology</span></div>
  <div class="benefit" style="left:627px"><div class="circle"><svg width="22" height="22" viewBox="0 0 22 22" fill="none" stroke="#1f5c63" stroke-width="1.6" stroke-linecap="round"><path d="M6 18h10M9 18c-3-1-3-6 0-7M10 4l3 1-2 6-3-1z"/></svg></div><h4>25+ Conditions</h4><span>Versatile application</span></div>
  <div class="benefit" style="left:919px"><div class="circle"><svg width="22" height="22" viewBox="0 0 22 22" fill="none" stroke="#1f5c63" stroke-width="1.6"><path d="M8 4h6v4h4v6h-4v4H8v-4H4V8h4z"/></svg></div><h4>Clinically Proven</h4><span>FDA cleared results</span></div>
</section>

<section class="results">
  <div class="eyebrow">TRANSFORMATIONS</div>
  <h2>Natural Evolution</h2>
  <p class="note">Real results after just one treatment session.</p>

  <div class="compare" style="left:32px">
    <div class="half" style="left:0;width:273px;background:linear-gradient(135deg,#6e5a4a,#a88670)" role="img" aria-label="Forehead skin before treatment"></div>
    <div class="half" style="left:273px;width:274px;background:linear-gradient(135deg,#b08e74,#8d7a68)" role="img" aria-label="Forehead skin after one treatment"></div>
    <div class="divider"></div>
    <div class="knob"><svg width="8" height="12" viewBox="0 0 8 12" fill="#1f5c63"><path d="M4 0l3 4H1zM4 12L1 8h6z"/></svg></div>
    <span class="tag" style="left:16px">BEFORE</span><span class="tag after" style="right:16px">AFTER 1 TREATMENT</span>
  </div>
  <div class="caption" style="left:32px">Full facial rejuvenation targeting rosacea and texture.</div>

  <div class="compare" style="left:623px">
    <div class="half" style="left:0;width:273px;background:linear-gradient(135deg,#3f3a36,#9a7a66)" role="img" aria-label="Cheek and smile lines before treatment"></div>
    <div class="half" style="left:273px;width:274px;background:linear-gradient(135deg,#c8a48c,#8a7a70)" role="img" aria-label="Cheek and smile lines after one treatment"></div>
    <div class="divider"></div>
    <div class="knob"><svg width="8" height="12" viewBox="0 0 8 12" fill="#1f5c63"><path d="M4 0l3 4H1zM4 12L1 8h6z"/></svg></div>
    <span class="tag" style="left:16px">BEFORE</span><span class="tag after" style="right:16px">AFTER 1 TREATMENT</span>
  </div>
  <div class="caption" style="left:623px">Lumexa precision smoothing for dynamic expression lines.</div>
</section>

<section class="pricing">
  <div class="price-card">
    <div class="wash"></div>
    <div class="price-copy">
      <h2>Affordable Clinical Care</h2>
      <p>We believe high-end skincare should be accessible. Our clinic operates on a direct-care model with transparent, competitive pricing.</p>
      <div class="perk"><span class="dot"><svg width="10" height="10" viewBox="0 0 10 10"><path d="M2 5l2 2 4-4" stroke="#1f5c63" stroke-width="1.5" fill="none"/></svg></span><div><h4>Cash-Pay Service</h4><p>Simple, direct payments. No insurance required or accepted, avoiding complex medical billing.</p></div></div>
      <div class="perk"><span class="dot"><svg width="10" height="10" viewBox="0 0 10 10"><rect x="1" y="2" width="8" height="6" rx="1" fill="#1f5c63"/></svg></span><div><h4>Exclusive Membership Rewards</h4><p class="teal">Special discounts and priority scheduling for 9 Vital members.</p></div></div>
    </div>
    <div class="package">
      <div class="eyebrow2">RECOMMENDED PATH</div>
      <div class="amount">$499</div>
      <div class="pkg">COMPREHENSIVE REJUVENATION PACKAGE</div>
      <div class="lines">
        <div class="line"><span>Qorvin Full Face Session</span><b>$350</b></div>
        <div class="line"><span>Lumexa (20 Units)</span><b>$240</b></div>
        <div class="line save"><span>Package Savings</span><span>-$91</span></div>
      </div>
      <span class="claim">Claim Member Pricing</span>
    </div>
  </div>
</section>

<section class="cta">
  <h2>Start with a personalized skin plan</h2>
  <p>Every skin journey begins with an expert clinical consultation. Let us design your roadmap to luminosity.</p>
  <div class="cta-actions">
    <span class="btn">Book My Consultation</span>
    <div class="phone">800-RADIANCE<small>LIMITED AVAILABILITY THIS WEEK</small></div>
  </div>
</section>

<footer class="footer">
  <div class="wordmark">9 Vital</div>
  <div class="legal">© 2026 RADIANT VITAL MEDICAL SKIN CLINIC. ALL RIGHTS RESERVED.</div>
  <nav><span>PRIVACY POLICY</span><span>TERMS OF SERVICE</span><span>CLINICAL SAFETY</span><span>CONTACT</span></nav>
</footer>

</body>
</html>
```